KESTIVA GROUP OF CLINICS

We need a medical & lab report file. The design should be healthcare related. Our current file design has been used for almost 10 years. We need something more fresh & up-to-date. We have attached the current file design.

```html
<!DOCTYPE html>
<html lang="en">
<head>
<meta charset="utf-8">
<title>Kestiva Group of Clinics – Medical Report Folder</title>
<link href="https://fonts.googleapis.com/css2?family=Poppins:wght@400;500;600;700;800&display=swap" rel="stylesheet">
<style>
  :root {
    --navy: #2e3192;
    --navy-soft: #4a4ea8;
    --cyan: #29a9e0;
    --cyan-light: #7fd3f2;
    --sky: #cdeefb;
    --sky-deep: #5cc3ec;
    --pale: #eef1f4;
    --white: #ffffff;
    --ghost: #e4e6f2;
    --stage: #d9dbe0;
  }
  * { margin: 0; padding: 0; box-sizing: border-box; }
  html, body { width: 842px; height: 1200px; overflow: hidden; background: var(--stage); }
  body { font-family: "Poppins", sans-serif; position: relative; }

  .spread { position: absolute; left: 0; width: 842px; height: 595px; display: flex; }
  .spread--outer { top: 0; }
  .spread--inner { top: 605px; }
  .panel { position: relative; width: 421px; height: 595px; overflow: hidden; }

  /* Back cover */
  .back-photo {
    position: absolute; inset: 0 0 125px 0;
    background: linear-gradient(160deg, #f3f5f7 0%, #dfe5ea 45%, #c9d6e0 100%);
  }
  .back-band {
    position: absolute; left: 0; right: 0; bottom: 60px; height: 70px;
    background: var(--cyan); color: var(--white);
    text-align: center; padding-top: 9px;
    font-size: 8.5px; line-height: 12px;
  }
  .back-band .web { font-weight: 700; letter-spacing: 3px; font-size: 10px; margin-top: 2px; }
  .back-foot { position: absolute; left: 0; right: 0; bottom: 0; height: 60px; background: var(--pale); }

  /* Front cover */
  .front-art {
    position: absolute; inset: 0;
    background:
      radial-gradient(circle at 72% 32%, rgba(255,255,255,0.85) 0%, rgba(255,255,255,0) 38%),
      linear-gradient(150deg, var(--sky-deep) 0%, var(--sky) 55%, var(--cyan-light) 100%);
  }
  .brand { position: absolute; left: 40px; top: 150px; display: flex; align-items: center; gap: 8px; }
  .brand__dot { width: 16px; height: 16px; border-radius: 50%; background: var(--navy); }
  .brand__name { color: var(--navy); font-weight: 700; font-size: 15px; letter-spacing: 0.5px; }
  .title { position: absolute; left: 38px; top: 230px; color: var(--navy); font-weight: 800; line-height: 0.95; }
  .title__line1 { font-size: 40px; }
  .title__line2 { font-size: 52px; }
  .tagline { position: absolute; left: 42px; top: 337px; color: var(--navy); font-weight: 700; font-size: 10px; }
  .front-band {
    position: absolute; left: 0; right: 0; bottom: 62px; height: 70px;
    background: var(--navy); text-align: center; padding-top: 12px;
  }
  .front-band .web { color: var(--white); font-weight: 700; font-size: 24px; letter-spacing: 3px; line-height: 28px; }
  .front-band .note { color: var(--cyan); font-size: 13px; line-height: 18px; }
  .front-foot { position: absolute; left: 0; right: 0; bottom: 0; height: 62px; background: linear-gradient(90deg, var(--cyan-light), var(--sky)); }

  /* Inside spread */
  .inside { background: var(--white); }
  .inside--left { border-right: 1px solid var(--pale); }
  .ghost-brand { position: absolute; left: 50%; top: 150px; transform: translateX(-50%); display: flex; align-items: center; gap: 10px; white-space: nowrap; }
  .ghost-brand__dot { width: 34px; height: 34px; border-radius: 50%; background: var(--ghost); }
  .ghost-brand__name { color: var(--ghost); font-weight: 700; font-size: 30px; }
  .pocket { position: absolute; left: 0; bottom: 0; width: 421px; height: 595px; }
</style>
</head>
<body>
  <section class="spread spread--outer">
    <article class="panel back-cover">
      <div class="back-photo" role="img" aria-label="Photo of a smiling doctor in a white coat standing beside a CT scanner"></div>
      <div class="back-band">
        <p>Level 4, Block C, Seri Harmoni Business Park</p>
        <p>Jalan Cendana 7/2, Section 7, 40450 Bandar Permata</p>
        <p>P. +603-1234 5678 &nbsp;M. +60 12-000 4471 &nbsp;E. admin@kestiva.my</p>
        <p class="web">WWW.KESTIVA.MY</p>
      </div>
      <div class="back-foot"></div>
    </article>

    <article class="panel front-cover">
      <div class="front-art" role="img" aria-label="Blue digital illustration of a translucent human body with skeleton over a medical interface background"></div>
      <div class="brand">
        <span class="brand__dot"></span>
        <span class="brand__name">KESTIVA GROUP</span>
      </div>
      <h1 class="title">
        <span class="title__line1">MEDICAL</span><br>
        <span class="title__line2">REPORT</span>
      </h1>
      <p class="tagline">YOUR HEALTHCARE PARTNER!</p>
      <div class="front-band">
        <p class="web">WWW.KESTIVA.MY</p>
        <p class="note">Private &amp; Confidential</p>
      </div>
      <div class="front-foot"></div>
    </article>
  </section>

  <section class="spread spread--inner">
    <article class="panel inside inside--left">
      <div class="ghost-brand">
        <span class="ghost-brand__dot"></span>
        <span class="ghost-brand__name">KESTIVA GROUP</span>
      </div>
      <svg class="pocket" viewBox="0 0 421 595" aria-hidden="true">
        <polygon points="0,350 421,430 421,595 0,595" fill="var(--navy)"/>
        <polygon points="0,350 421,430 421,440 0,362" fill="var(--navy-soft)"/>
      </svg>
    </article>
    <article class="panel inside inside--right">
      <div class="ghost-brand">
        <span class="ghost-brand__dot"></span>
        <span class="ghost-brand__name">KESTIVA GROUP</span>
      </div>
      <svg class="pocket" viewBox="0 0 421 595" aria-hidden="true">
        <polygon points="0,430 421,350 421,595 0,595" fill="var(--navy)"/>
        <polygon points="0,430 421,350 421,362 0,440" fill="var(--navy-soft)"/>
      </svg>
    </article>
  </section>
</body>
</html>
```